Talents and colours poster for home office

The objective is to illustrate/communicate and remember 5 talents and 4 colours of the personality.

The infographic will be hanged on the wall of an home office. It need to be simple and clear. Illustrations and pictograms can be used. It can be artistic.

Here's the content:

5 talents,scaling in priority from #1 to #5
Ideation / creativity
Winning other over / charisma
Adaptability
Positivity
Empathy

In the files there is a description of what those mean.

You have to include 4 colours, scaling in priority from #1 to #4
Yellow
Green
Red
Blue

I made a sketch just for fun... and to show why I need professionnal skills :)

THX

Office

• offensive materials

```html
<!DOCTYPE html>
<html lang="en">
<head>
<meta charset="utf-8">
<title>Talents and Colours Poster</title>
<link href="https://fonts.googleapis.com/css2?family=Oregano:ital@0;1&display=swap" rel="stylesheet">
<style>
  :root {
    --backdrop: #eceae6;
    --paper-top: #fbfaf6;
    --paper-bottom: #b9dbe9;
    --yellow: #f6c21a;
    --orange: #f07a1c;
    --green-light: #74c13a;
    --green-dark: #2e8a2c;
    --red-light: #f1355c;
    --red-dark: #d01a2e;
    --violet-light: #9a8ee0;
    --violet-dark: #5d6bd6;
    --blue-light: #4a64e8;
    --blue-dark: #1f2fb8;
    --label: #ffffff;
    --label-shade: rgba(40, 20, 30, 0.55);
  }
  html, body {
    margin: 0;
    padding: 0;
    width: 1087px;
    height: 1200px;
    overflow: hidden;
    background: var(--backdrop);
  }
  .canvas {
    position: relative;
    width: 1087px;
    height: 1200px;
  }
  .poster {
    position: absolute;
    left: 141px;
    top: 30px;
    width: 804px;
    height: 1140px;
    display: block;
  }
  .talent-circle {
    mix-blend-mode: multiply;
  }
  .talent-label {
    font-family: "Oregano", cursive;
    font-size: 50px;
    fill: var(--label);
    text-anchor: middle;
    filter: drop-shadow(1.5px 2px 1.5px var(--label-shade));
  }
</style>
</head>
<body>
<div class="canvas">
  <svg class="poster" viewBox="0 0 605 858" xmlns="http://www.w3.org/2000/svg" aria-label="Five talents poster">
    <defs>
      <linearGradient id="paper" x1="0" y1="0" x2="0" y2="1">
        <stop offset="0" stop-color="var(--paper-top)"/>
        <stop offset="0.55" stop-color="var(--paper-top)"/>
        <stop offset="1" stop-color="var(--paper-bottom)"/>
      </linearGradient>
      <radialGradient id="wash-ideation" cx="0.5" cy="0.7" r="0.6">
        <stop offset="0" stop-color="var(--yellow)"/>
        <stop offset="0.55" stop-color="#f5a21a"/>
        <stop offset="1" stop-color="var(--orange)"/>
      </radialGradient>
      <radialGradient id="wash-charisma" cx="0.35" cy="0.4" r="0.7">
        <stop offset="0" stop-color="var(--green-light)"/>
        <stop offset="1" stop-color="var(--green-dark)"/>
      </radialGradient>
      <radialGradient id="wash-adaptability" cx="0.5" cy="0.5" r="0.6">
        <stop offset="0" stop-color="var(--red-light)"/>
        <stop offset="1" stop-color="var(--red-dark)"/>
      </radialGradient>
      <radialGradient id="wash-positivity" cx="0.55" cy="0.45" r="0.65">
        <stop offset="0" stop-color="var(--violet-light)"/>
        <stop offset="1" stop-color="var(--violet-dark)"/>
      </radialGradient>
      <radialGradient id="wash-empathy" cx="0.5" cy="0.5" r="0.6">
        <stop offset="0" stop-color="var(--blue-light)"/>
        <stop offset="1" stop-color="var(--blue-dark)"/>
      </radialGradient>
      <clipPath id="sheet">
        <rect x="0" y="0" width="605" height="858"/>
      </clipPath>
    </defs>

    <rect class="paper" x="0" y="0" width="605" height="858" fill="url(#paper)"/>

    <g clip-path="url(#sheet)">
      <circle class="talent-circle" cx="420" cy="130" r="210" fill="url(#wash-ideation)" opacity="0.95"/>
      <circle class="talent-circle" cx="180" cy="318" r="180" fill="url(#wash-charisma)" opacity="0.92"/>
      <circle class="talent-circle" cx="446" cy="420" r="168" fill="url(#wash-adaptability)" opacity="0.9"/>
      <circle class="talent-circle" cx="172" cy="648" r="183" fill="url(#wash-positivity)" opacity="0.85"/>
      <circle class="talent-circle" cx="440" cy="705" r="168" fill="url(#wash-empathy)" opacity="0.9"/>
    </g>

    <text class="talent-label" x="425" y="120">Ideation /</text>
    <text class="talent-label" x="425" y="186">Creativity</text>

    <text class="talent-label" x="140" y="255">Winning</text>
    <text class="talent-label" x="145" y="315">other over</text>
    <text class="talent-label" x="150" y="376">/ Charisma</text>

    <text class="talent-label" x="458" y="480">Adaptability</text>
    <text class="talent-label" x="152" y="636">Positivity</text>
    <text class="talent-label" x="440" y="742">Empathy</text>
  </svg>
</div>
</body>
</html>
```